Amber Ridge Productions

I need a business card design for a new freelance film production company using or incorporating the logo:
I want the card to be creative, minimal, yet professional. Feel free to use a variety of different shapes and sizes/ textures for the card.

Industry/Entity Type

Film Production

```html
<!DOCTYPE html>
<html lang="en">
<head>
<meta charset="utf-8">
<title>Amber Ridge Productions – Business Card</title>
<link rel="stylesheet" href="https://fonts.googleapis.com/css2?family=Libre+Baskerville:wght@700&display=swap">
<style>
  :root {
    --stage: #ececec;
    --paper: #ffffff;
    --brand-blue: #1f47e0;
    --navy: #0d2170;
    --sky: #c3cdf3;
    --strip: #1b1b22;
    --ink: #151515;
    --white: #ffffff;
    --text-font: "Libre Baskerville", serif;
  }
  * { box-sizing: border-box; margin: 0; padding: 0; }
  html, body { width: 1200px; height: 780px; overflow: hidden; background: var(--stage); }
  .canvas { position: relative; width: 1200px; height: 780px; font-family: var(--text-font); font-weight: 700; }

  .card {
    position: absolute; top: 235px; width: 540px; height: 310px;
    box-shadow: 0 6px 18px rgba(0,0,0,.18);
    overflow: hidden;
  }

  /* Front */
  .card-front { left: 40px; background: var(--paper); display: flex; align-items: center; justify-content: center; }
  .brand-name { font-size: 26px; color: var(--brand-blue); text-align: center; line-height: 1.3; }

  /* Back */
  .card-back { left: 620px; background: var(--sky); }
  .back-brand {
    position: absolute; left: 0; top: 0; width: 200px; height: 100%;
    background: var(--navy); display: flex; align-items: center; justify-content: center; padding: 0 14px;
  }
  .back-brand .brand-name { font-size: 17px; color: var(--white); }

  .film-strip { position: absolute; left: 200px; top: 0; width: 50px; height: 100%; background: var(--strip); }

  .identity { position: absolute; left: 285px; width: 220px; top: 78px; text-align: center; color: var(--ink); }
  .identity .person { font-size: 15px; letter-spacing: 1px; padding-bottom: 3px; border-bottom: 1.5px solid var(--ink); }
  .identity .role { font-size: 11px; margin-top: 8px; }

  .contacts { position: absolute; left: 0; top: 175px; width: 540px; list-style: none; color: var(--ink); }
  .contacts li { position: relative; height: 23px; font-size: 9.5px; }
  .contacts .leader { position: absolute; left: 250px; width: 38px; border-top: 1px solid var(--ink); top: 11px; }
  .contacts .icon { position: absolute; left: 288px; top: 4px; width: 15px; height: 15px; }
  .contacts .value { position: absolute; left: 310px; top: 5px; white-space: nowrap; }
</style>
</head>
<body>
<main class="canvas">

  <section class="card card-front" aria-label="Card front">
    <p class="brand-name">Amber Ridge Productions</p>
  </section>

  <section class="card card-back" aria-label="Card back">
    <div class="back-brand">
      <p class="brand-name">Amber Ridge Productions</p>
    </div>

    <div class="film-strip" role="img" aria-label="Vertical film strip ornament"></div>

    <div class="identity">
      <div class="person">Your Name</div>
      <div class="role">CEO</div>
    </div>

    <ul class="contacts">
      <li>
        <span class="leader"></span>
        <svg class="icon" viewBox="0 0 14 14" aria-hidden="true">
          <circle cx="7" cy="7" r="6.3" fill="none" stroke="var(--ink)" stroke-width="1.2"/>
          <path d="M4.6 3.6l1.4 1.6-.7 1c.5 1 1.2 1.7 2.2 2.2l1-.7 1.6 1.4-.9 1.2C6.6 10 4 7.4 3.7 4.5z" fill="var(--ink)"/>
        </svg>
        <span class="value">(123) 456-7890</span>
      </li>
      <li>
        <span class="leader"></span>
        <svg class="icon" viewBox="0 0 14 14" aria-hidden="true"><circle cx="7" cy="7" r="6.3" fill="var(--ink)"/></svg>
        <span class="value">@AmberRidgeFilms</span>
      </li>
      <li>
        <span class="leader"></span>
        <svg class="icon" viewBox="0 0 14 14" aria-hidden="true"><rect x="1" y="1" width="12" height="12" fill="var(--ink)"/></svg>
        <span class="value">/amberridgefilms</span>
      </li>
      <li>
        <span class="leader"></span>
        <svg class="icon" viewBox="0 0 14 14" aria-hidden="true">
          <circle cx="7" cy="7" r="6.3" fill="none" stroke="var(--ink)" stroke-width="1.2"/>
          <rect x="3.5" y="4.5" width="7" height="5" fill="none" stroke="var(--ink)" stroke-width="1"/>
          <path d="M3.5 4.5L7 7.3l3.5-2.8" fill="none" stroke="var(--ink)" stroke-width="1"/>
        </svg>
        <span class="value">hello@amberridgeproduction.com</span>
      </li>
      <li>
        <span class="leader"></span>
        <svg class="icon" viewBox="0 0 14 14" aria-hidden="true">
          <circle cx="7" cy="7" r="6.3" fill="none" stroke="var(--ink)" stroke-width="1.2"/>
          <ellipse cx="7" cy="7" rx="2.6" ry="6.3" fill="none" stroke="var(--ink)" stroke-width="1"/>
          <line x1=".7" y1="7" x2="13.3" y2="7" stroke="var(--ink)" stroke-width="1"/>
        </svg>
        <span class="value">www.amberridgeproduction.com</span>
      </li>
    </ul>
  </section>

</main>
</body>
</html>
```